Forensic Psychology and Polygraph Needs Clever Catchy Logo

There's a massive trade show coming up and we are looking to debut a new, clever logo for our business cards. We are a private practice that offers psychological evaluations, therapeutic counseling, and polygraphing. Our website is kelvora.net (to get a better idea of the color scheme) and instead of the nature/cuddly image that other psychology organizations like to go for, we are interested in cultivating a business, strength, and professional image.
Attached are some popular logos and designs to get those creative juices flowing! I would like to avoid the brain/psi logo as this has been to death so bonus points definitely for originality.
Target Market(s)
governmental agencies, third party mental health providers, individual private pay clients
Industry/Entity Type
Mental Health
Contact Information for Business Card
One one side will be the logo and company name while on the back will be contact information and provider details (name, position, etc)
Look and feel
Each slider illustrates characteristics of the customer's brand and the style your logo design should communicate.

```html
<!DOCTYPE html>
<html lang="en">
<head>
<meta charset="utf-8">
<title>Marlow &amp; Associates – Business Card</title>
<link href="https://fonts.googleapis.com/css2?family=Lato:wght@300;400&display=swap" rel="stylesheet">
<style>
  :root {
    --page-bg: #2b2b2b;
    --card-top: #2a2a2a;
    --card-bottom: #151515;
    --ink: #ffffff;
    --ink-muted: #b5b5b5;
    --photo-light: #3a3a3a;
    --photo-dark: #0d0d0d;
  }
  * { margin: 0; padding: 0; box-sizing: border-box; }
  html, body { width: 1200px; height: 1200px; overflow: hidden; }
  body {
    background: var(--page-bg);
    font-family: "Lato", sans-serif;
    color: var(--ink);
    display: flex;
    flex-direction: column;
    align-items: center;
    justify-content: center;
    gap: 40px;
  }
  .card {
    position: relative;
    width: 1000px;
    height: 540px;
    background: linear-gradient(160deg, var(--card-top), var(--card-bottom));
    box-shadow: 0 12px 30px rgba(0,0,0,.5);
    overflow: hidden;
  }
  .brand {
    font-weight: 400;
    color: var(--ink);
  }
  .brand-name { font-size: 44px; letter-spacing: 1px; }
  .brand-tagline {
    font-weight: 300;
    font-size: 22px;
    letter-spacing: 9px;
    color: var(--ink-muted);
    margin-top: 4px;
  }
  .card-front .brand {
    position: absolute;
    inset: 0;
    display: flex;
    flex-direction: column;
    align-items: center;
    justify-content: center;
    text-align: center;
  }
  .card-back .backdrop { position: absolute; inset: 0; }
  .card-back .brand {
    position: absolute;
    left: 90px;
    top: 250px;
  }
  .provider {
    position: absolute;
    right: 60px;
    top: 60px;
    text-align: right;
  }
  .provider-name { font-size: 46px; font-weight: 400; letter-spacing: 3px; }
  .provider-role { font-size: 20px; font-weight: 300; letter-spacing: 2px; color: var(--ink-muted); }
  .contact-list {
    position: absolute;
    left: 610px;
    top: 250px;
    list-style: none;
  }
  .contact-item {
    display: flex;
    align-items: flex-start;
    gap: 16px;
    font-size: 22px;
    font-weight: 300;
    line-height: 1.2;
    margin-bottom: 18px;
  }
  .contact-icon { flex: none; width: 32px; height: 32px; }
</style>
</head>
<body>

  <section class="card card-front">
    <div class="brand">
      <div class="brand-name">Marlow &amp; Associates</div>
      <div class="brand-tagline">Psychological Services</div>
    </div>
  </section>

  <section class="card card-back">
    <svg class="backdrop" viewBox="0 0 1000 540" width="1000" height="540">
      <defs>
        <linearGradient id="cityTone" x1="0" y1="0" x2="0" y2="1">
          <stop offset="0" stop-color="var(--photo-light)"/>
          <stop offset="1" stop-color="var(--photo-dark)"/>
        </linearGradient>
        <linearGradient id="lightBand" x1="0" y1="0" x2="1" y2="1">
          <stop offset="0" stop-color="#ffffff" stop-opacity=".10"/>
          <stop offset="1" stop-color="#ffffff" stop-opacity="0"/>
        </linearGradient>
      </defs>
      <polygon role="img" aria-label="Night city skyline reflected on water"
               points="0,90 430,90 560,200 390,540 0,540" fill="url(#cityTone)"/>
      <polygon points="430,90 520,60 640,150 560,200" fill="url(#lightBand)"/>
    </svg>

    <div class="brand">
      <div class="brand-name">Marlow &amp; Associates</div>
      <div class="brand-tagline">Psychological Services</div>
    </div>

    <div class="provider">
      <div class="provider-name">JORDAN MARLOW</div>
      <div class="provider-role">Licensed Psychologist</div>
    </div>

    <ul class="contact-list">
      <li class="contact-item">
        <svg class="contact-icon" viewBox="0 0 32 32"><circle cx="16" cy="16" r="16" fill="var(--ink)"/><path d="M11 9l3 0 1 4-2 1.5a9 9 0 0 0 4.5 4.5L19 17l4 1 0 3a2 2 0 0 1-2 2A12 12 0 0 1 9 11a2 2 0 0 1 2-2z" fill="#222"/></svg>
        <span>555 210 3384</span>
      </li>
      <li class="contact-item">
        <svg class="contact-icon" viewBox="0 0 32 32"><circle cx="16" cy="16" r="16" fill="var(--ink)"/><rect x="8" y="11" width="16" height="11" fill="none" stroke="#222" stroke-width="1.8"/><path d="M8 11l8 6 8-6" fill="none" stroke="#222" stroke-width="1.8"/></svg>
        <span>contact@kelvora.net</span>
      </li>
      <li class="contact-item">
        <svg class="contact-icon" viewBox="0 0 32 32"><circle cx="16" cy="16" r="16" fill="var(--ink)"/><circle cx="16" cy="16" r="8" fill="none" stroke="#222" stroke-width="1.8"/><ellipse cx="16" cy="16" rx="3.5" ry="8" fill="none" stroke="#222" stroke-width="1.5"/><path d="M8 16h16" stroke="#222" stroke-width="1.5"/></svg>
        <span>www.kelvora.net</span>
      </li>
      <li class="contact-item">
        <svg class="contact-icon" viewBox="0 0 32 32"><circle cx="16" cy="16" r="16" fill="var(--ink)"/><path d="M16 25s-6-6.5-6-11a6 6 0 0 1 12 0c0 4.5-6 11-6 11z" fill="#222"/><circle cx="16" cy="14" r="2.2" fill="var(--ink)"/></svg>
        <span>2280 W. Cedar Ridge Rd.<br>Suites 204 &amp; 208, Tempe,<br>Arizona 85281</span>
      </li>
    </ul>
  </section>

</body>
</html>
```